Etiketten-Design für Imkerei
Super Zusammenarbeit. Änderungswünsche wurden sofort berücksichtigt und bearbeitet. Sind mit dem Design richtig happy und können Friederike nur weiterempfehlen.
Zielgruppe
Wir sind eine kleine aber feine Imkerei, die gerade erst begonnen hat. Deshalb sind wir auf der Suche nach einem ansprechenden Design um einen guten Eindruck zu hinterlassen.
Aufgabenstellung
Das Design für unsere Imkerei Wabenglanz sollte möglichst schlicht in den Farben sein . Da wir die Imkerei zu zweit führen, wäre es cool wenn man Elemente einbauen könnte, die darauf hinweisen. (zb.: 2 Blumen, 2 Bienen, 2 Honigtöpfe, 2 Bäume....je nach dem). Wir hätten uns vorgestellt, dass eine verspielte Biene herumschwirrt. Wir werden eine Skizze anfügen, lassen uns aber von eigenen Ideen gerne überzeugen. Außerdem bitte ich auf die Kennzeichnungsverordnung, die in Österreich gilt, acht zu geben. Schriftgröße bei Mengenangabe ist sehr wichtig (wird angefügt).
Wir benötigen die Etiketten in 2 verschiedenen Größen (250g und 500g gleiches Etikett mit 40x140mm(Höhe x Breite), 1000g mit 60x190mm(Höhe x Breite)) jeweils für Blütenhonig und Cremehonig
Wir freuen uns auf viele spannende Entwürfe, sind für alles offen und bedanken uns im Voraus.

```html
<!DOCTYPE html>
<html lang="de">
<head>
<meta charset="utf-8">
<title>Wabenglanz – Honigetiketten</title>
<link rel="stylesheet" href="https://fonts.googleapis.com/css2?family=Oswald:wght@300;400;500;600&display=swap">
<style>
  :root {
    --honey: #fcd333;
    --honey-soft: #fde27a;
    --ink: #0b0b0b;
    --paper: #ffffff;
    --backdrop: #ececec;
  }
  * { box-sizing: border-box; margin: 0; padding: 0; }
  html, body {
    width: 1200px; height: 820px; overflow: hidden;
    background: var(--backdrop);
    font-family: "Oswald", "Arial Narrow", sans-serif;
    color: var(--ink);
  }
  .canvas {
    position: relative; width: 1200px; height: 820px;
    display: flex; justify-content: center; align-items: center; gap: 80px;
  }
  .label {
    position: relative; width: 440px; height: 440px;
    background: var(--paper); overflow: hidden;
  }
  .label__band {
    position: absolute; top: 0; left: 0; right: 0; height: 45px;
    background: var(--ink); color: var(--paper);
    display: flex; align-items: center; justify-content: center;
    font-weight: 400; font-size: 31px; line-height: 1;
  }
  .label__band span { display: inline-block; transform: scaleX(0.84); white-space: nowrap; }

  /* front */
  .honey-art {
    position: absolute; top: 45px; left: 0; width: 440px; height: 320px;
    background: linear-gradient(172deg, var(--honey) 0%, var(--honey) 52%, var(--honey-soft) 72%, var(--paper) 100%);
  }
  .brand {
    position: absolute; top: 128px; left: 0; right: 0;
    display: flex; justify-content: center; align-items: center; gap: 12px;
  }
  .brand__dot { width: 14px; height: 14px; border-radius: 50%; background: var(--ink); }
  .brand__name { font-weight: 500; font-size: 50px; line-height: 1; }
  .weight {
    position: absolute; top: 238px; left: 0; right: 0; text-align: center;
    font-weight: 600; font-size: 34px; line-height: 1;
  }
  .variety {
    position: absolute; bottom: 10px; left: 0; right: 0; text-align: center;
    font-weight: 600; font-size: 33px; line-height: 1;
  }
  .variety span { display: inline-block; transform: scaleX(0.88); }

  /* back */
  .honey-corner {
    position: absolute; top: 45px; right: 0; width: 220px; height: 90px;
    background: linear-gradient(200deg, var(--honey) 0%, var(--honey) 40%, var(--honey-soft) 70%, var(--paper) 100%);
  }
  .info {
    position: absolute; top: 56px; left: 12px; right: 22px;
    font-weight: 400; font-size: 33px; line-height: 40px;
  }
  .info__line { display: block; white-space: nowrap; transform: scaleX(0.82); transform-origin: left; }
  .info__line--strong { font-weight: 600; }
  .info__gap { height: 32px; }
  .info__blank {
    display: inline-block; width: 150px; border-bottom: 2px solid var(--ink);
    vertical-align: baseline;
  }
</style>
</head>
<body>
<main class="canvas">

  <section class="label label--front">
    <div class="honey-art" role="img" aria-label="Illustration: tropfender Honig mit zwei verspielten Bienen und gestrichelter Herz-Flugspur"></div>
    <div class="label__band"><span>ÖSTERREICHISCHER BIENENHONIG</span></div>
    <div class="brand">
      <span class="brand__dot"></span>
      <span class="brand__name">Wabenglanz</span>
    </div>
    <div class="weight">250g</div>
    <div class="variety"><span>Blütenhonig</span></div>
  </section>

  <section class="label label--back">
    <div class="honey-corner" role="img" aria-label="Illustration: tropfender Honig in der Ecke"></div>
    <div class="label__band"></div>
    <div class="info">
      <span class="info__line info__line--strong">Imkerei Wabenglanz</span>
      <span class="info__line">Lindenweg 12</span>
      <span class="info__line">3542 Kleinfeld</span>
      <span class="info__line">www.wabenglanz.at</span>
      <div class="info__gap"></div>
      <span class="info__line">Vor Licht und Wärme geschützt lagern!</span>
      <span class="info__line">Mindestens haltbar bis:<span class="info__blank"></span></span>
      <span class="info__line">L 123456</span>
      <span class="info__line">Ursprungsland: Österreich</span>
    </div>
  </section>

</main>
</body>
</html>
```